Business card design needed

am looking for a fun and funky design to match our moto, seriously fun swimwear and fashion for girls.

We manufacture and retail girls swimwear and fashion in Australia. Our designs are fun loving and funky. I would like to use bright fuschia to match our website www.breezyplum.com.au. We target a higher end market so need it to reflect this.

Industry/Entity Type

Fashion

Contact Information for Business Card

Breezy Plum logo,
Melanie Harte
(07) 35912847
admin@breezyplum.com.au
www.breezyplum.com.au

Logo Text

Breezy Plum

```html
<!DOCTYPE html>
<html lang="en">
<head>
<meta charset="utf-8">
<title>Breezy Plum — Business Card</title>
<link rel="stylesheet" href="https://fonts.googleapis.com/css2?family=Barlow:wght@300;400&display=swap">
<style>
  :root {
    --page: #ffffff;
    --fuchsia: #e819dc;
    --fuchsia-deep: #d316c8;
    --ink: #ffffff;
  }
  html, body {
    margin: 0;
    padding: 0;
    width: 1200px;
    height: 900px;
    overflow: hidden;
    background: var(--page);
  }
  .canvas {
    position: relative;
    width: 1200px;
    height: 900px;
  }
  .card {
    position: absolute;
    left: 69px;
    top: 144px;
    width: 1063px;
    height: 614px;
    background: var(--fuchsia);
    overflow: hidden;
    font-family: "Barlow", sans-serif;
    color: var(--ink);
  }
  .card__pattern {
    position: absolute;
    inset: 0;
    background: radial-gradient(circle at 726px 401px,
      var(--fuchsia-deep) 0%,
      var(--fuchsia) 70%);
  }
  .brand-name {
    position: absolute;
    left: 72px;
    top: 67px;
    margin: 0;
    font-size: 120px;
    font-weight: 300;
    line-height: 1;
    letter-spacing: 1px;
    white-space: nowrap;
  }
  .contact {
    position: absolute;
    right: 79px;
    top: 374px;
    margin: 0;
    text-align: right;
    font-style: normal;
    font-weight: 300;
    white-space: nowrap;
  }
  .contact__name {
    display: block;
    font-size: 46px;
    line-height: 58px;
    margin-bottom: 5px;
  }
  .contact__line {
    display: block;
    font-size: 32px;
    line-height: 39px;
    letter-spacing: 0.5px;
  }
</style>
</head>
<body>
  <main class="canvas">
    <section class="card">
      <div class="card__pattern" role="img" aria-label="Decorative swirl pattern in deep fuchsia tones"></div>
      <h1 class="brand-name">Breezy Plum</h1>
      <address class="contact">
        <span class="contact__name">Melanie Harte</span>
        <span class="contact__line">(07) 35912847</span>
        <span class="contact__line">admin@breezyplum.com.au</span>
        <span class="contact__line">www.breezyplum.com.au</span>
      </address>
    </section>
  </main>
</body>
</html>
```